Design für einen Jahresplaner gesucht
Zielgruppe
Scannen und Designen Zahntechnischer und Zahnmedizinischer Arbeiten und das Fräsen und 3d Drucken von bereits in CAD konstruierten Objekten. Wir verfügen über die modernsten Zahntechnischen Technologien und bieten diese als Dienstleister für Dentallabore an.
Aufgabenstellung
Wir benotigen ein Jahresplaner für unsere Kunden. Die Beigefügte Vorlage dient regelrecht nur der Grösenvorlage.
Das Design soll Technisch und Innovativ sein. Gleischzeitig aber gradlinig und nicht zu verspielt.
Das Logo kann ruhig stark ins Auge fallen. Die Schriftfarben sollen überwigen dunkelgrau sein. Hervorzuhebende Bereiche wie z. B. Sonntage, Feiertage sollten die Logofaben beinhalten. Bilder können auch verwendet werden aber wir würden uns über ein Schönes Layout ohne Bilder auch freuen.
PS: Unter dem Logo muss in Feiner Schrift stehen
eine Marke der Norvak GmbH

```html
<!DOCTYPE html>
<html lang="de">
<head>
<meta charset="utf-8">
<title>2019 Jahresplaner</title>
<link rel="stylesheet" href="https://fonts.googleapis.com/css2?family=Poppins:wght@400;500;600;700&display=swap">
<style>
:root{
  --page:#e6e7e9;
  --sheet:#f7f9fb;
  --sheet-tint:#e4edf3;
  --ink:#4a4a4a;
  --ink-soft:#7a7d80;
  --rule:#c7cbcf;
  --month:#9ccbe1;
  --weekend:#f8e5c2;
  --holiday:#b0186a;
  --brand:#3a9fd6;
}
*{margin:0;padding:0;box-sizing:border-box}
html,body{width:948px;height:1200px;overflow:hidden}
body{background:var(--page);font-family:"Poppins",sans-serif;color:var(--ink)}
.planner{
  position:absolute;left:0;top:250px;width:948px;height:700px;
  background:linear-gradient(135deg,var(--sheet) 0%,var(--sheet-tint) 45%,var(--sheet) 70%,var(--sheet-tint) 100%);
  padding:36px 70px 0;
}
.planner-head{display:flex;align-items:center;height:64px}
.brand{width:240px}
.brand-name{display:flex;align-items:center;gap:8px;font-size:30px;font-weight:500;color:var(--ink);line-height:1}
.brand-dot{width:26px;height:26px;border-radius:50%;background:var(--brand)}
.brand-claim{font-size:7px;color:var(--ink-soft);margin:4px 0 0 34px;letter-spacing:.2px}
.planner-title{font-size:35px;font-weight:700;color:var(--ink);letter-spacing:.5px}
.calendar{display:grid;grid-template-columns:repeat(12,1fr);column-gap:8px;margin-top:18px}
.month h2{height:17px;background:var(--month);color:#fff;font-size:8.5px;font-weight:600;text-align:center;line-height:17px;border-radius:2px 2px 0 0;margin-bottom:2px}
.month ol{list-style:none}
.month li{position:relative;height:17px;border-bottom:1px solid var(--rule)}
.month li.weekend{background:var(--weekend)}
.month b{position:absolute;left:2px;top:1px;font-size:7.5px;font-weight:500;color:var(--ink)}
.month small{position:absolute;left:2px;bottom:1px;font-size:3.6px;color:var(--ink-soft);white-space:nowrap;text-transform:uppercase}
.month em{position:absolute;right:2px;bottom:2px;font-size:5px;font-style:normal;color:var(--ink-soft)}
.month li.holiday b{color:var(--holiday);font-weight:700}
</style>
</head>
<body>
<section class="planner">
  <header class="planner-head">
    <div class="brand">
      <div class="brand-name"><span class="brand-dot"></span>Dentrafo</div>
      <p class="brand-claim">eine Marke der Norvak GmbH</p>
    </div>
    <h1 class="planner-title">2019 JAHRESPLANER</h1>
  </header>
  <div class="calendar">
    <div class="month"><h2>JANUAR</h2><ol>
      <li class="holiday"><b>1</b><small>DI Neujahr</small></li><li><b>2</b><small>MI</small></li><li><b>3</b><small>DO</small></li><li><b>4</b><small>FR</small></li><li class="weekend"><b>5</b><small>SA</small></li><li class="weekend"><b>6</b><small>SO</small></li><li><b>7</b><small>MO</small><em>2</em></li><li><b>8</b><small>DI</small></li><li><b>9</b><small>MI</small></li><li><b>10</b><small>DO</small></li><li><b>11</b><small>FR</small></li><li class="weekend"><b>12</b><small>SA</small></li><li class="weekend"><b>13</b><small>SO</small></li><li><b>14</b><small>MO</small><em>3</em></li><li><b>15</b><small>DI</small></li><li><b>16</b><small>MI</small></li><li><b>17</b><small>DO</small></li><li><b>18</b><small>FR</small></li><li class="weekend"><b>19</b><small>SA</small></li><li class="weekend"><b>20</b><small>SO</small></li><li><b>21</b><small>MO</small><em>4</em></li><li><b>22</b><small>DI</small></li><li><b>23</b><small>MI</small></li><li><b>24</b><small>DO</small></li><li><b>25</b><small>FR</small></li><li class="weekend"><b>26</b><small>SA</small></li><li class="weekend"><b>27</b><small>SO</small></li><li><b>28</b><small>MO</small><em>5</em></li><li><b>29</b><small>DI</small></li><li><b>30</b><small>MI</small></li><li><b>31</b><small>DO</small></li>
    </ol></div>
    <div class="month"><h2>FEBRUAR</h2><ol>
      <li><b>1</b><small>FR</small></li><li class="weekend"><b>2</b><small>SA</small></li><li class="weekend"><b>3</b><small>SO</small></li><li><b>4</b><small>MO</small><em>6</em></li><li><b>5</b><small>DI</small></li><li><b>6</b><small>MI</small></li><li><b>7</b><small>DO</small></li><li><b>8</b><small>FR</small></li><li class="weekend"><b>9</b><small>SA</small></li><li class="weekend"><b>10</b><small>SO</small></li><li><b>11</b><small>MO</small><em>7</em></li><li><b>12</b><small>DI</small></li><li><b>13</b><small>MI</small></li><li><b>14</b><small>DO</small></li><li><b>15</b><small>FR</small></li><li class="weekend"><b>16</b><small>SA</small></li><li class="weekend"><b>17</b><small>SO</small></li><li><b>18</b><small>MO</small><em>8</em></li><li><b>19</b><small>DI</small></li><li><b>20</b><small>MI</small></li><li><b>21</b><small>DO</small></li><li><b>22</b><small>FR</small></li><li class="weekend"><b>23</b><small>SA</small></li><li class="weekend"><b>24</b><small>SO</small></li><li><b>25</b><small>MO</small><em>9</em></li><li><b>26</b><small>DI</small></li><li><b>27</b><small>MI</small></li><li><b>28</b><small>DO</small></li>
    </ol></div>
    <div class="month"><h2>MÄRZ</h2><ol>
      <li><b>1</b><small>FR</small></li><li class="weekend"><b>2</b><small>SA</small></li><li class="weekend"><b>3</b><small>SO</small></li><li><b>4</b><small>MO</small><em>10</em></li><li><b>5</b><small>DI</small></li><li><b>6</b><small>MI</small></li><li><b>7</b><small>DO</small></li><li><b>8</b><small>FR</small></li><li class="weekend"><b>9</b><small>SA</small></li><li class="weekend"><b>10</b><small>SO</small></li><li><b>11</b><small>MO</small><em>11</em></li><li><b>12</b><small>DI</small></li><li><b>13</b><small>MI</small></li><li><b>14</b><small>DO</small></li><li><b>15</b><small>FR</small></li><li class="weekend"><b>16</b><small>SA</small></li><li class="weekend"><b>17</b><small>SO</small></li><li><b>18</b><small>MO</small><em>12</em></li><li><b>19</b><small>DI</small></li><li><b>20</b><small>MI</small></li><li><b>21</b><small>DO</small></li><li><b>22</b><small>FR</small></li><li class="weekend"><b>23</b><small>SA</small></li><li class="weekend"><b>24</b><small>SO</small></li><li><b>25</b><small>MO</small><em>13</em></li><li><b>26</b><small>DI</small></li><li><b>27</b><small>MI</small></li><li><b>28</b><small>DO</small></li><li><b>29</b><small>FR</small></li><li class="weekend"><b>30</b><small>SA</small></li><li class="weekend"><b>31</b><small>SO</small></li>
    </ol></div>
    <div class="month"><h2>APRIL</h2><ol>
      <li><b>1</b><small>MO</small><em>14</em></li><li><b>2</b><small>DI</small></li><li><b>3</b><small>MI</small></li><li><b>4</b><small>DO</small></li><li><b>5</b><small>FR</small></li><li class="weekend"><b>6</b><small>SA</small></li><li class="weekend"><b>7</b><small>SO</small></li><li><b>8</b><small>MO</small><em>15</em></li><li><b>9</b><small>DI</small></li><li><b>10</b><small>MI</small></li><li><b>11</b><small>DO</small></li><li><b>12</b><small>FR</small></li><li class="weekend"><b>13</b><small>SA</small></li><li class="weekend"><b>14</b><small>SO</small></li><li><b>15</b><small>MO</small><em>16</em></li><li><b>16</b><small>DI</small></li><li><b>17</b><small>MI</small></li><li><b>18</b><small>DO</small></li><li class="holiday"><b>19</b><small>FR Karfreitag</small></li><li class="weekend"><b>20</b><small>SA</small></li><li class="weekend"><b>21</b><small>SO</small></li><li class="holiday"><b>22</b><small>MO Ostermontag</small><em>17</em></li><li><b>23</b><small>DI</small></li><li><b>24</b><small>MI</small></li><li><b>25</b><small>DO</small></li><li><b>26</b><small>FR</small></li><li class="weekend"><b>27</b><small>SA</small></li><li class="weekend"><b>28</b><small>SO</small></li><li><b>29</b><small>MO</small><em>18</em></li><li><b>30</b><small>DI</small></li>
    </ol></div>
    <div class="month"><h2>MAI</h2><ol>
      <li class="holiday"><b>1</b><small>MI Tag der Arbeit</small></li><li><b>2</b><small>DO</small></li><li><b>3</b><small>FR</small></li><li class="weekend"><b>4</b><small>SA</small></li><li class="weekend"><b>5</b><small>SO</small></li><li><b>6</b><small>MO</small><em>19</em></li><li><b>7</b><small>DI</small></li><li><b>8</b><small>MI</small></li><li><b>9</b><small>DO</small></li><li><b>10</b><small>FR</small></li><li class="weekend"><b>11</b><small>SA</small></li><li class="weekend"><b>12</b><small>SO</small></li><li><b>13</b><small>MO</small><em>20</em></li><li><b>14</b><small>DI</small></li><li><b>15</b><small>MI</small></li><li><b>16</b><small>DO</small></li><li><b>17</b><small>FR</small></li><li class="weekend"><b>18</b><small>SA</small></li><li class="weekend"><b>19</b><small>SO</small></li><li><b>20</b><small>MO</small><em>21</em></li><li><b>21</b><small>DI</small></li><li><b>22</b><small>MI</small></li><li><b>23</b><small>DO</small></li><li><b>24</b><small>FR</small></li><li class="weekend"><b>25</b><small>SA</small></li><li class="weekend"><b>26</b><small>SO</small></li><li><b>27</b><small>MO</small><em>22</em></li><li><b>28</b><small>DI</small></li><li><b>29</b><small>MI</small></li><li class="holiday"><b>30</b><small>DO Christi Himmelfahrt</small></li><li><b>31</b><small>FR</small></li>
    </ol></div>
    <div class="month"><h2>JUNI</h2><ol>
      <li class="weekend"><b>1</b><small>SA</small></li><li class="weekend"><b>2</b><small>SO</small></li><li><b>3</b><small>MO</small><em>23</em></li><li><b>4</b><small>DI</small></li><li><b>5</b><small>MI</small></li><li><b>6</b><small>DO</small></li><li><b>7</b><small>FR</small></li><li class="weekend"><b>8</b><small>SA</small></li><li class="weekend holiday"><b>9</b><small>SO Pfingstsonntag</small></li><li class="holiday"><b>10</b><small>MO Pfingstmontag</small><em>24</em></li><li><b>11</b><small>DI</small></li><li><b>12</b><small>MI</small></li><li><b>13</b><small>DO</small></li><li><b>14</b><small>FR</small></li><li class="weekend"><b>15</b><small>SA</small></li><li class="weekend"><b>16</b><small>SO</small></li><li><b>17</b><small>MO</small><em>25</em></li><li><b>18</b><small>DI</small></li><li><b>19</b><small>MI</small></li><li><b>20</b><small>DO</small></li><li><b>21</b><small>FR</small></li><li class="weekend"><b>22</b><small>SA</small></li><li class="weekend"><b>23</b><small>SO</small></li><li><b>24</b><small>MO</small><em>26</em></li><li><b>25</b><small>DI</small></li><li><b>26</b><small>MI</small></li><li><b>27</b><small>DO</small></li><li><b>28</b><small>FR</small></li><li class="weekend"><b>29</b><small>SA</small></li><li class="weekend"><b>30</b><small>SO</small></li>
    </ol></div>
    <div class="month"><h2>JULI</h2><ol>
      <li><b>1</b><small>MO</small><em>27</em></li><li><b>2</b><small>DI</small></li><li><b>3</b><small>MI</small></li><li><b>4</b><small>DO</small></li><li><b>5</b><small>FR</small></li><li class="weekend"><b>6</b><small>SA</small></li><li class="weekend"><b>7</b><small>SO</small></li><li><b>8</b><small>MO</small><em>28</em></li><li><b>9</b><small>DI</small></li><li><b>10</b><small>MI</small></li><li><b>11</b><small>DO</small></li><li><b>12</b><small>FR</small></li><li class="weekend"><b>13</b><small>SA</small></li><li class="weekend"><b>14</b><small>SO</small></li><li><b>15</b><small>MO</small><em>29</em></li><li><b>16</b><small>DI</small></li><li><b>17</b><small>MI</small></li><li><b>18</b><small>DO</small></li><li><b>19</b><small>FR</small></li><li class="weekend"><b>20</b><small>SA</small></li><li class="weekend"><b>21</b><small>SO</small></li><li><b>22</b><small>MO</small><em>30</em></li><li><b>23</b><small>DI</small></li><li><b>24</b><small>MI</small></li><li><b>25</b><small>DO</small></li><li><b>26</b><small>FR</small></li><li class="weekend"><b>27</b><small>SA</small></li><li class="weekend"><b>28</b><small>SO</small></li><li><b>29</b><small>MO</small><em>31</em></li><li><b>30</b><small>DI</small></li><li><b>31</b><small>MI</small></li>
    </ol></div>
    <div class="month"><h2>AUGUST</h2><ol>
      <li><b>1</b><small>DO</small></li><li><b>2</b><small>FR</small></li><li class="weekend"><b>3</b><small>SA</small></li><li class="weekend"><b>4</b><small>SO</small></li><li><b>5</b><small>MO</small><em>32</em></li><li><b>6</b><small>DI</small></li><li><b>7</b><small>MI</small></li><li><b>8</b><small>DO</small></li><li><b>9</b><small>FR</small></li><li class="weekend"><b>10</b><small>SA</small></li><li class="weekend"><b>11</b><small>SO</small></li><li><b>12</b><small>MO</small><em>33</em></li><li><b>13</b><small>DI</small></li><li><b>14</b><small>MI</small></li><li><b>15</b><small>DO</small></li><li><b>16</b><small>FR</small></li><li class="weekend"><b>17</b><small>SA</small></li><li class="weekend"><b>18</b><small>SO</small></li><li><b>19</b><small>MO</small><em>34</em></li><li><b>20</b><small>DI</small></li><li><b>21</b><small>MI</small></li><li><b>22</b><small>DO</small></li><li><b>23</b><small>FR</small></li><li class="weekend"><b>24</b><small>SA</small></li><li class="weekend"><b>25</b><small>SO</small></li><li><b>26</b><small>MO</small><em>35</em></li><li><b>27</b><small>DI</small></li><li><b>28</b><small>MI</small></li><li><b>29</b><small>DO</small></li><li><b>30</b><small>FR</small></li><li class="weekend"><b>31</b><small>SA</small></li>
    </ol></div>
    <div class="month"><h2>SEPTEMBER</h2><ol>
      <li class="weekend"><b>1</b><small>SO</small></li><li><b>2</b><small>MO</small><em>36</em></li><li><b>3</b><small>DI</small></li><li><b>4</b><small>MI</small></li><li><b>5</b><small>DO</small></li><li><b>6</b><small>FR</small></li><li class="weekend"><b>7</b><small>SA</small></li><li class="weekend"><b>8</b><small>SO</small></li><li><b>9</b><small>MO</small><em>37</em></li><li><b>10</b><small>DI</small></li><li><b>11</b><small>MI</small></li><li><b>12</b><small>DO</small></li><li><b>13</b><small>FR</small></li><li class="weekend"><b>14</b><small>SA</small></li><li class="weekend"><b>15</b><small>SO</small></li><li><b>16</b><small>MO</small><em>38</em></li><li><b>17</b><small>DI</small></li><li><b>18</b><small>MI</small></li><li><b>19</b><small>DO</small></li><li><b>20</b><small>FR</small></li><li class="weekend"><b>21</b><small>SA</small></li><li class="weekend"><b>22</b><small>SO</small></li><li><b>23</b><small>MO</small><em>39</em></li><li><b>24</b><small>DI</small></li><li><b>25</b><small>MI</small></li><li><b>26</b><small>DO</small></li><li><b>27</b><small>FR</small></li><li class="weekend"><b>28</b><small>SA</small></li><li class="weekend"><b>29</b><small>SO</small></li><li><b>30</b><small>MO</small><em>40</em></li>
    </ol></div>
    <div class="month"><h2>OKTOBER</h2><ol>
      <li><b>1</b><small>DI</small></li><li><b>2</b><small>MI</small></li><li class="holiday"><b>3</b><small>DO Tag der Dt. Einheit</small></li><li><b>4</b><small>FR</small></li><li class="weekend"><b>5</b><small>SA</small></li><li class="weekend"><b>6</b><small>SO</small></li><li><b>7</b><small>MO</small><em>41</em></li><li><b>8</b><small>DI</small></li><li><b>9</b><small>MI</small></li><li><b>10</b><small>DO</small></li><li><b>11</b><small>FR</small></li><li class="weekend"><b>12</b><small>SA</small></li><li class="weekend"><b>13</b><small>SO</small></li><li><b>14</b><small>MO</small><em>42</em></li><li><b>15</b><small>DI</small></li><li><b>16</b><small>MI</small></li><li><b>17</b><small>DO</small></li><li><b>18</b><small>FR</small></li><li class="weekend"><b>19</b><small>SA</small></li><li class="weekend"><b>20</b><small>SO</small></li><li><b>21</b><small>MO</small><em>43</em></li><li><b>22</b><small>DI</small></li><li><b>23</b><small>MI</small></li><li><b>24</b><small>DO</small></li><li><b>25</b><small>FR</small></li><li class="weekend"><b>26</b><small>SA</small></li><li class="weekend"><b>27</b><small>SO</small></li><li><b>28</b><small>MO</small><em>44</em></li><li><b>29</b><small>DI</small></li><li><b>30</b><small>MI</small></li><li><b>31</b><small>DO</small></li>
    </ol></div>
    <div class="month"><h2>NOVEMBER</h2><ol>
      <li><b>1</b><small>FR</small></li><li class="weekend"><b>2</b><small>SA</small></li><li class="weekend"><b>3</b><small>SO</small></li><li><b>4</b><small>MO</small><em>45</em></li><li><b>5</b><small>DI</small></li><li><b>6</b><small>MI</small></li><li><b>7</b><small>DO</small></li><li><b>8</b><small>FR</small></li><li class="weekend"><b>9</b><small>SA</small></li><li class="weekend"><b>10</b><small>SO</small></li><li><b>11</b><small>MO</small><em>46</em></li><li><b>12</b><small>DI</small></li><li><b>13</b><small>MI</small></li><li><b>14</b><small>DO</small></li><li><b>15</b><small>FR</small></li><li class="weekend"><b>16</b><small>SA</small></li><li class="weekend"><b>17</b><small>SO</small></li><li><b>18</b><small>MO</small><em>47</em></li><li><b>19</b><small>DI</small></li><li><b>20</b><small>MI</small></li><li><b>21</b><small>DO</small></li><li><b>22</b><small>FR</small></li><li class="weekend"><b>23</b><small>SA</small></li><li class="weekend"><b>24</b><small>SO</small></li><li><b>25</b><small>MO</small><em>48</em></li><li><b>26</b><small>DI</small></li><li><b>27</b><small>MI</small></li><li><b>28</b><small>DO</small></li><li><b>29</b><small>FR</small></li><li class="weekend"><b>30</b><small>SA</small></li>
    </ol></div>
    <div class="month"><h2>DEZEMBER</h2><ol>
      <li class="weekend"><b>1</b><small>SO</small></li><li><b>2</b><small>MO</small><em>49</em></li><li><b>3</b><small>DI</small></li><li><b>4</b><small>MI</small></li><li><b>5</b><small>DO</small></li><li><b>6</b><small>FR</small></li><li class="weekend"><b>7</b><small>SA</small></li><li class="weekend"><b>8</b><small>SO</small></li><li><b>9</b><small>MO</small><em>50</em></li><li><b>10</b><small>DI</small></li><li><b>11</b><small>MI</small></li><li><b>12</b><small>DO</small></li><li><b>13</b><small>FR</small></li><li class="weekend"><b>14</b><small>SA</small></li><li class="weekend"><b>15</b><small>SO</small></li><li><b>16</b><small>MO</small><em>51</em></li><li><b>17</b><small>DI</small></li><li><b>18</b><small>MI</small></li><li><b>19</b><small>DO</small></li><li><b>20</b><small>FR</small></li><li class="weekend"><b>21</b><small>SA</small></li><li class="weekend"><b>22</b><small>SO</small></li><li><b>23</b><small>MO</small><em>52</em></li><li><b>24</b><small>DI</small></li><li class="holiday"><b>25</b><small>MI 1. Weihnachtstag</small></li><li class="holiday"><b>26</b><small>DO 2. Weihnachtstag</small></li><li><b>27</b><small>FR</small></li><li class="weekend"><b>28</b><small>SA</small></li><li class="weekend"><b>29</b><small>SO</small></li><li><b>30</b><small>MO</small><em>53</em></li><li><b>31</b><small>DI</small></li>
    </ol></div>
  </div>
</section>
</body>
</html>
```